Silver Meadow Renewal needs a Business Card Design

We need a business card design for a new company based in Queensland, Australia using our new logo (attached) using similar or complimentary colours and showing a softness and honesty. On the back we would like space to write three appointment or session times.ie. Session 1.... Session 2... Session 3.

Industry/Entity Type

Business

Contact Information for Business Card

name, title, mobile, email, web, address, facebook,

Requirements
Must have
• on back of card must have following:
• For information about Vibranomic Therapy please visit www.velmorashift.com
• Please use the registered symbol of an R in a circle at end of Vibranomic Therapy please.

```html
<!DOCTYPE html>
<html lang="en">
<head>
<meta charset="utf-8">
<title>Silver Meadow Renewal – Business Card</title>
<link rel="stylesheet" href="https://fonts.googleapis.com/css2?family=Questrial&display=swap">
<style>
  :root {
    --page-bg: #ece8e1;
    --card-white: #ffffff;
    --brand-blue: #1f7fd0;
    --brand-blue-deep: #1b5fb8;
    --brand-cyan: #4cc6e6;
    --brand-green: #9fcd5a;
    --text-dark: #2b2b2b;
    --text-mid: #555555;
    --line-light: rgba(255,255,255,0.75);
    --card-shadow: 0 10px 28px rgba(0,0,0,0.22);
  }
  * { box-sizing: border-box; margin: 0; padding: 0; }
  html, body {
    width: 1200px; height: 858px; overflow: hidden;
    background: var(--page-bg);
    font-family: "Questrial", "Century Gothic", sans-serif;
  }
  .canvas { position: relative; width: 1200px; height: 858px; }

  .card {
    position: absolute;
    width: 560px; height: 320px;
    border-radius: 4px;
    overflow: hidden;
    box-shadow: var(--card-shadow);
  }

  /* Front */
  .card-front { left: 60px; top: 90px; background: var(--card-white); }
  .card-front .swoosh { position: absolute; inset: 0; width: 100%; height: 100%; }

  .brand {
    position: absolute; left: 34px; top: 110px;
    display: flex; align-items: center; gap: 10px;
  }
  .brand-dot {
    flex: 0 0 auto;
    width: 30px; height: 30px; border-radius: 50%;
    background: var(--brand-blue);
  }
  .brand-name {
    font-size: 19px; letter-spacing: 0.5px;
    color: var(--brand-blue); text-transform: uppercase;
    white-space: nowrap;
  }
  .tagline {
    position: absolute; left: 74px; top: 142px;
    font-size: 14px; color: var(--brand-green);
  }

  .person { position: absolute; left: 34px; top: 176px; }
  .person-name { font-size: 21px; color: var(--text-dark); }
  .person-title { font-size: 10.5px; color: var(--text-mid); line-height: 1.35; margin-top: 2px; }

  .contacts { position: absolute; left: 34px; top: 226px; list-style: none; }
  .contacts li {
    display: flex; align-items: center; gap: 8px;
    font-size: 12px; color: var(--text-dark); height: 19px;
  }
  .contact-icon {
    width: 15px; height: 15px; border-radius: 50%;
    border: 1.5px solid var(--brand-blue);
    display: flex; align-items: center; justify-content: center;
  }
  .contact-icon svg { width: 8px; height: 8px; fill: var(--brand-green); }

  /* Back */
  .card-back {
    left: 580px; top: 450px;
    background: linear-gradient(160deg, var(--brand-blue-deep) 0%, var(--brand-blue) 45%, var(--brand-cyan) 100%);
    color: #ffffff;
  }
  .back-web {
    position: absolute; left: 28px; top: 0; height: 100%;
    writing-mode: vertical-rl;
    display: flex; align-items: center; justify-content: center;
    font-size: 14px; white-space: nowrap;
  }
  .back-content {
    position: absolute; left: 86px; right: 36px; top: 30px; bottom: 24px;
    display: flex; flex-direction: column;
  }
  .back-brand { display: flex; align-items: center; gap: 12px; }
  .back-brand .brand-dot { width: 34px; height: 34px; background: #ffffff; }
  .back-brand .brand-name { color: #ffffff; font-size: 18px; }

  .sessions { list-style: none; margin-top: 26px; }
  .sessions li {
    display: flex; align-items: flex-end; gap: 10px;
    font-size: 14px; height: 36px;
  }
  .sessions .session-line {
    flex: 1; border-bottom: 1px dotted var(--line-light);
    margin-bottom: 3px;
  }
  .back-info {
    margin-top: auto;
    font-size: 11.5px; line-height: 1.45;
  }
</style>
</head>
<body>
<main class="canvas">

  <section class="card card-front" aria-label="Business card front">
    <svg class="swoosh" viewBox="0 0 560 320" preserveAspectRatio="none" aria-hidden="true">
      <defs>
        <linearGradient id="band-blue" x1="0" y1="0" x2="1" y2="1">
          <stop offset="0" stop-color="#1b6fcb"/>
          <stop offset="1" stop-color="#3bb0e0"/>
        </linearGradient>
      </defs>
      <rect width="560" height="320" fill="url(#band-blue)"/>
      <ellipse cx="190" cy="360" rx="370" ry="330" fill="#9fcd5a"/>
      <ellipse cx="150" cy="380" rx="360" ry="350" fill="#ffffff"/>
    </svg>

    <div class="brand">
      <span class="brand-dot"></span>
      <span class="brand-name">Silver Meadow Renewal</span>
    </div>
    <p class="tagline">with Vibranomic Therapy®</p>

    <div class="person">
      <p class="person-name">Maren Holloway</p>
      <p class="person-title">Vibranomic Therapy Foundational Practitioner<br>&amp; Velmora Certified Practitioner</p>
    </div>

    <ul class="contacts">
      <li><span class="contact-icon"><svg viewBox="0 0 10 10"><path d="M2 0.5h2l1 2.5-1.3 1a6 6 0 0 0 2.3 2.3l1-1.3 2.5 1v2a1 1 0 0 1-1 1A8.5 8.5 0 0 1 0.5 1.5a1 1 0 0 1 1-1z"/></svg></span>0412 306 948</li>
      <li><span class="contact-icon"><svg viewBox="0 0 10 10"><path d="M0.5 2h9v6h-9z M0.5 2l4.5 3.5 4.5-3.5" fill="none" stroke="#9fcd5a" stroke-width="1.2"/></svg></span>maren@silvermeadowrenewal.com.au</li>
      <li><span class="contact-icon"><svg viewBox="0 0 10 10"><circle cx="5" cy="5" r="4" fill="none" stroke="#9fcd5a" stroke-width="1.2"/><path d="M1 5h8M5 1c-2 2.5-2 5.5 0 8M5 1c2 2.5 2 5.5 0 8" fill="none" stroke="#9fcd5a" stroke-width="0.9"/></svg></span>www.silvermeadowrenewal.com.au</li>
      <li><span class="contact-icon"><svg viewBox="0 0 10 10"><path d="M5 0.5a3.3 3.3 0 0 1 3.3 3.3C8.3 6.3 5 9.5 5 9.5S1.7 6.3 1.7 3.8A3.3 3.3 0 0 1 5 0.5zm0 2a1.3 1.3 0 1 0 0 2.6 1.3 1.3 0 0 0 0-2.6z"/></svg></span>14 Wattlebrook Rd, Kenmore Vale, Qld 4520</li>
    </ul>
  </section>

  <section class="card card-back" aria-label="Business card back">
    <p class="back-web">www.silvermeadowrenewal.com.au</p>
    <div class="back-content">
      <div class="back-brand">
        <span class="brand-dot"></span>
        <span class="brand-name">Silver Meadow Renewal</span>
      </div>
      <ul class="sessions">
        <li>Session 1 <span class="session-line"></span></li>
        <li>Session 2 <span class="session-line"></span></li>
        <li>Session 3 <span class="session-line"></span></li>
      </ul>
      <p class="back-info">For information about Vibranomic Therapy® please visit www.velmorashift.com</p>
    </div>
  </section>

</main>
</body>
</html>
```